Postcard Design for Fertility & Pregnancy Clinic

We are an Australian acupuncture clinic which specialises in treating women who are trying to get pregnant or are already pregnant. The postcard will be attached to our signage outside the building to be taken by prospective clients. We want to convey a professional but welcoming impression. We also want it to look a bit different from the usual pregnancy and fertility type images, e.g. no baby pictures. The signage they are going to be attached to is red so they will probably need to be a different colour to stand out from that which we would probably prefer to be green but are open to other suggestions.

Target Market(s)

Women 25 - 45 years

Industry/Entity Type

Alternative Medicine

Requirements
Must have
• Vertical design, front and back of the postcard with the text on the back of the card
Nice to have
• I like illustrations more than photos.
Should not have
• Generic baby or pregnancy photos

```html
<!DOCTYPE html>
<html lang="en">
<head>
<meta charset="utf-8">
<title>Willowmere Acupuncture Clinic – Postcard Back</title>
<link href="https://fonts.googleapis.com/css2?family=Open+Sans:wght@400;600;700&family=Arimo:wght@700&family=Michroma&display=swap" rel="stylesheet">
<style>
  :root {
    --backdrop: #3a3a3a;
    --red: #ff1408;
    --lime: #80ff00;
    --white: #ffffff;
    --green-dark: #1d7a10;
    --green-mid: #2aa616;
    --bullet: #8cff1a;
  }
  * { margin: 0; padding: 0; box-sizing: border-box; }
  html, body { width: 955px; height: 1200px; overflow: hidden; }
  body { background: var(--backdrop); position: relative; font-family: "Open Sans", sans-serif; }

  .card {
    position: absolute; left: 69px; top: 69px;
    width: 817px; height: 1062px; background: var(--white);
  }
  .intro-panel {
    position: absolute; left: 0; top: 0; width: 100%; height: 568px;
    background: var(--red); color: var(--white);
  }
  .intro-text {
    position: absolute; left: 43px; top: 42px; width: 740px;
    font-size: 21.5px; line-height: 32px; font-weight: 400;
  }
  .conditions-title {
    position: absolute; left: 41px; top: 222px;
    font-size: 26px; font-weight: 700;
  }
  .conditions-list {
    position: absolute; top: 272px; list-style: none;
    font-size: 21px; font-weight: 700;
  }
  .conditions-list.left { left: 46px; }
  .conditions-list.right { left: 424px; }
  .conditions-list li {
    height: 37px; line-height: 30px; padding-left: 22px; position: relative; white-space: nowrap;
  }
  .conditions-list li::before {
    content: ""; position: absolute; left: 0; top: 10px;
    width: 11px; height: 11px; border-radius: 50%; background: var(--bullet);
  }

  .cta-band {
    position: absolute; left: 0; top: 568px; width: 100%; height: 98px;
    background: var(--lime); color: var(--white);
    font-family: "Arimo", sans-serif; font-weight: 700; font-size: 20px;
    line-height: 28px; text-align: center; text-transform: uppercase;
    padding-top: 24px;
  }

  .brand {
    position: absolute; left: 138px; top: 694px; height: 126px;
    display: flex; align-items: center; gap: 14px;
  }
  .brand-dot { width: 124px; height: 124px; border-radius: 50%; background: var(--green-mid); }
  .brand-name {
    color: var(--red); font-weight: 400; font-size: 32px; line-height: 38px;
  }

  .phone {
    position: absolute; left: 0; top: 842px; width: 100%;
    display: flex; justify-content: center; align-items: center; gap: 12px;
    color: var(--green-dark); font-family: "Michroma", sans-serif; font-size: 48px;
  }
  .contact-line {
    position: absolute; left: 0; width: 100%;
    display: flex; justify-content: center; align-items: center; gap: 8px;
    color: var(--green-dark); font-family: "Arimo", sans-serif; font-weight: 700;
  }
  .website { top: 906px; font-size: 20.5px; }
  .email { top: 945px; font-size: 18px; }
  .address { top: 983px; font-size: 18px; line-height: 24px; text-align: center; }
</style>
</head>
<body>
  <article class="card">
    <section class="intro-panel">
      <p class="intro-text">Acupuncture is an effective and safe method of improving your general health in order to increase your chances of conceiving and/or of having the pregnancy you desire. We combine our acupuncture techniques with lots of lifestyle and nutritional advice tailored just for you.</p>
      <h2 class="conditions-title">Common conditions we see at the clinic include:</h2>
      <ul class="conditions-list left">
        <li>PCOS</li>
        <li>Endometriosis</li>
        <li>Irregular or no periods</li>
        <li>Poor ovarian reserve</li>
        <li>Recurrent implantation failure</li>
        <li>IVF Support</li>
        <li>Embryo transfer treatments</li>
      </ul>
      <ul class="conditions-list right">
        <li>Stress and anxiety</li>
        <li>Morning sickness</li>
        <li>Breech babies</li>
        <li>Hip and back pain in pregnancy</li>
        <li>Carpel tunnel</li>
        <li>Pre-birth acupuncture</li>
        <li>Natural induction of labour</li>
      </ul>
    </section>

    <section class="cta-band">
      Please check out the website for further information<br>or give us a call if you’d like an appointment.
    </section>

    <div class="brand">
      <span class="brand-dot"></span>
      <span class="brand-name">Willowmere<br>Acupuncture Clinic</span>
    </div>

    <div class="phone">
      <svg width="40" height="40" viewBox="0 0 40 40" aria-hidden="true">
        <circle cx="20" cy="20" r="17" fill="none" stroke="#80ff00" stroke-width="3"/>
        <path d="M14 11c1.5-1 2.5-.5 3.3 1l1.3 2.6c.5 1 .2 2-.7 2.6l-1 .7c.8 2 2.3 3.6 4.2 4.6l.8-1c.7-.9 1.7-1.1 2.6-.6l2.6 1.4c1.4.8 1.7 1.9.7 3.2-1.3 1.7-3.3 2.2-5.4 1.3-4.6-2-8-5.6-9.6-10.2-.7-2.1-.3-4 1.2-5.6z" fill="none" stroke="#80ff00" stroke-width="2"/>
      </svg>
      <span>07 3555 0194</span>
    </div>

    <div class="contact-line website">
      <svg width="20" height="20" viewBox="0 0 20 20" aria-hidden="true">
        <g fill="none" stroke="#80ff00" stroke-width="1.8">
          <circle cx="10" cy="10" r="8"/><ellipse cx="10" cy="10" rx="3.5" ry="8"/>
          <line x1="2" y1="10" x2="18" y2="10"/>
        </g>
      </svg>
      <span>WWW.WILLOWMEREACUPUNCTURECLINIC.COM.AU</span>
    </div>

    <div class="contact-line email">
      <svg width="22" height="16" viewBox="0 0 22 16" aria-hidden="true">
        <g fill="none" stroke="#80ff00" stroke-width="1.8">
          <rect x="1" y="1" width="20" height="14"/><path d="M1 1l10 8 10-8"/>
        </g>
      </svg>
      <span>hello@willowmereacupunctureclinic.com.au</span>
    </div>

    <div class="contact-line address">
      <svg width="14" height="20" viewBox="0 0 14 20" aria-hidden="true" style="align-self:flex-start;margin-top:2px">
        <path d="M7 1a6 6 0 0 1 6 6c0 4.5-6 12-6 12S1 11.5 1 7a6 6 0 0 1 6-6z" fill="none" stroke="#80ff00" stroke-width="1.6"/>
        <circle cx="7" cy="7" r="2" fill="none" stroke="#80ff00" stroke-width="1.4"/>
      </svg>
      <span>Level 6, Harwood Medical Centre, 148 Marlow Tce,<br>Kelvin Grove, Qld, 4059.</span>
    </div>
  </article>
</body>
</html>
```